Mindfulness School for Children -- Business Cards

We're looking for business cards for our school directors and owners. We're a mindfulness school for children called little compass. Attached are our logos/icons.

```html
<!DOCTYPE html>
<html lang="en">
<head>
<meta charset="utf-8">
<title>little compass — business cards</title>
<link href="https://fonts.googleapis.com/css2?family=Alegreya:wght@400&family=Arimo:wght@400;700&display=swap" rel="stylesheet">
<style>
  :root {
    --bg: #c9c9c9;
    --card: #262627;
    --card-deep: #111112;
    --edge: #3fb2c6;
    --teal: #4fb3c8;
    --mint: #84ccb3;
    --text: #f1f1f1;
    --emblem: #2e2e30;
    --divider: #6fbfae;
  }
  * { box-sizing: border-box; margin: 0; padding: 0; }
  html, body { width: 1200px; height: 788px; overflow: hidden; }
  body {
    background: var(--bg);
    display: flex;
    align-items: center;
    justify-content: center;
    gap: 40px;
    font-family: "Arimo", Arial, sans-serif;
  }
  .card {
    position: relative;
    width: 560px;
    height: 320px;
    border-radius: 22px;
    background: var(--card);
    border-bottom: 4px solid var(--edge);
    box-shadow: 0 14px 28px rgba(0,0,0,.25);
    overflow: hidden;
  }
  /* front */
  .emblem-area {
    position: absolute;
    left: 40px; top: 70px;
    width: 210px; height: 190px;
    border-radius: 18px;
    background: radial-gradient(circle at 50% 40%, #38383a, var(--emblem) 70%);
  }
  .divider {
    position: absolute;
    left: 276px; top: 58px;
    width: 1px; height: 204px;
    background: linear-gradient(var(--card), var(--divider) 40%, var(--divider) 70%, var(--card));
  }
  .details {
    position: absolute;
    left: 300px; top: 62px;
    color: var(--text);
  }
  .brand-name {
    font-family: "Alegreya", Georgia, serif;
    font-size: 30px;
    color: var(--mint);
    line-height: 1;
    margin-bottom: 18px;
  }
  .person-name {
    font-weight: 700;
    font-size: 20px;
    letter-spacing: .5px;
    color: var(--teal);
  }
  .person-title {
    font-size: 13px;
    margin: 4px 0 18px;
  }
  .contact-list { list-style: none; }
  .contact-list li {
    display: flex;
    align-items: center;
    gap: 8px;
    font-size: 12.5px;
    margin-bottom: 8px;
  }
  .contact-list svg { width: 12px; height: 12px; fill: var(--teal); flex: none; }
  /* back */
  .pattern-area {
    position: absolute;
    inset: 0;
    background: linear-gradient(215deg, #9a9a9a 0%, #5a5a5c 25%, #2a2a2c 50%, var(--card-deep) 80%);
  }
  .back-brand {
    position: absolute;
    right: 50px; bottom: 70px;
    font-family: "Alegreya", Georgia, serif;
    font-size: 46px;
    color: var(--mint);
    line-height: 1;
  }
</style>
</head>
<body>

  <section class="card card-front">
    <div class="emblem-area" role="img" aria-label="Large embossed emblem decoration"></div>
    <div class="divider"></div>
    <div class="details">
      <p class="brand-name">little compass</p>
      <p class="person-name">NORA WHITFIELD</p>
      <p class="person-title">CEO/Founder</p>
      <ul class="contact-list">
        <li>
          <svg viewBox="0 0 24 24" aria-hidden="true"><path d="M6.6 10.8a15 15 0 0 0 6.6 6.6l2.2-2.2a1 1 0 0 1 1-.25 11.4 11.4 0 0 0 3.6.57 1 1 0 0 1 1 1V20a1 1 0 0 1-1 1A17 17 0 0 1 3 4a1 1 0 0 1 1-1h3.5a1 1 0 0 1 1 1c0 1.25.2 2.45.57 3.57a1 1 0 0 1-.25 1z"/></svg>
          (00) 5820 3196
        </li>
        <li>
          <svg viewBox="0 0 24 24" aria-hidden="true"><path d="M2 5h20v14H2zm2 2v.5l8 5 8-5V7l-8 5z"/></svg>
          hello@littlecompass.com
        </li>
        <li>
          <svg viewBox="0 0 24 24" aria-hidden="true"><circle cx="12" cy="12" r="10"/></svg>
          www.littlecompass.com
        </li>
      </ul>
    </div>
  </section>

  <section class="card card-back">
    <div class="pattern-area" role="img" aria-label="Repeating glossy emblem pattern fading from grey to black"></div>
    <p class="back-brand">little compass</p>
  </section>

</body>
</html>
```